International IT and cyber security consulting company is looking to establish a web presence.

Halvern Ridge Advisory LLC provides IT, cyber security, risk, project management and data analytics consulting services worldwide. Our clients are both government and corporate. We are looking to establish a basic web presence with about 6 pages (Home, About Halvern, Our Experts, News and Events, Careers, Contact Us). The designs should set the look and feel of the site for further build out down the line. The final design should be straightforward and simple and allow us to convey information about our consulting services clearly.

Target Market(s)

Government and corporate clients or potential clients, job seekers.

Industry/Entity Type

Consulting

Contact Information for Business Card

The cards will have english on the front and arabic on the back. The design should be the same on both sides.

Coding

Number of Pages Required

Font styles to use
Serif
Sans Serif

Requirements
Must have
• The pages should be simple but visually appealing with a picture or graphic that is appropriate to the company or services we offer. Our name and logo should be branded throughout the design. While we are mostly an IT company we also have a line of business where we organize speaking events for VIPs so the website shouldn't overly emphasize our IT work.
Should not have
• No cartoons or drawings. The site should not have overly flashy or loud colors. We cater to a conservative set of clients so the site should match what they expect to see in an international consultancy's website. There should not be an overuse of the color orange because it can be hard on the eyes if it is used too much on the page. Also, please do not use graphics or pictures that use locks, keys, castles, shields etc since these are too commonly used in the cyber security industry.

```html
<!DOCTYPE html>
<html lang="en">
<head>
<meta charset="utf-8">
<title>Halvern Ridge Advisory LLC</title>
<link href="https://fonts.googleapis.com/css2?family=Merriweather:wght@400;700;900&family=Open+Sans:wght@400;600;700&display=swap" rel="stylesheet">
<style>
:root{
  --orange:#f58a3c;
  --ink:#2b2b2b;
  --text:#6f6f6f;
  --light:#efefef;
  --dark:#262626;
  --darker:#1c1c1c;
  --white:#fff;
  --sans:'Open Sans',Arial,sans-serif;
  --serif:'Merriweather',Georgia,serif;
}
*{box-sizing:border-box;margin:0;padding:0}
html,body{width:1200px;height:5391px;overflow:hidden}
body{font-family:var(--serif);color:var(--text);background:var(--white)}
.section{position:relative;width:1200px;overflow:hidden}
.abs{position:absolute}
.eyebrow{font-family:var(--sans);font-size:9px;color:var(--orange);text-transform:uppercase;letter-spacing:.3px}
.title{font-family:var(--sans);font-weight:600;color:var(--ink);font-size:25px}
.center{text-align:center;left:0;width:1200px}
.body{font-size:11px;line-height:22px}
.logo{display:flex;align-items:center;gap:8px;font-family:var(--serif);color:var(--orange);font-size:14px;line-height:16px;width:170px}
.logo-mark{width:14px;height:14px;background:var(--orange);flex:none}

/* top bar & nav */
.topbar{top:0;left:0;width:1200px;height:38px;background:var(--darker);font-family:var(--sans);font-size:10px;color:#ddd;z-index:2}
.topbar .item{position:absolute;top:12px;display:flex;align-items:center;gap:6px}
.social{position:absolute;top:9px;width:18px;height:18px;background:#555}
.nav{top:38px;left:0;width:1200px;height:94px;background:rgba(30,30,30,.72);z-index:2}
.nav .logo{position:absolute;left:161px;top:31px}
.menu{position:absolute;right:161px;top:40px;display:flex;gap:25px;font-family:var(--sans);font-size:11px;color:#eee}
.menu .active{color:var(--orange)}

/* hero */
.hero{height:806px;background:
  radial-gradient(ellipse 180px 220px at 1000px 230px,rgba(214,170,140,.45),transparent 70%),
  radial-gradient(ellipse 260px 180px at 600px 540px,rgba(120,165,220,.55),transparent 70%),
  radial-gradient(ellipse 200px 300px at 1110px 520px,rgba(220,225,230,.35),transparent 70%),
  radial-gradient(ellipse 300px 260px at 220px 250px,rgba(70,80,95,.6),transparent 70%),
  linear-gradient(115deg,#1f252d 0%,#2f3a48 35%,#46566a 55%,#333d4a 80%,#1b2027 100%)}
.hero .eyebrow{left:161px;top:349px;font-size:10px;letter-spacing:.6px}
.hero h1{position:absolute;left:161px;top:368px;font-family:var(--serif);font-weight:900;font-size:36px;color:var(--white);letter-spacing:.3px}
.hero p{position:absolute;left:161px;top:432px;width:560px;font-size:11px;line-height:22px;color:var(--white);font-weight:700}
.btn{position:absolute;background:var(--orange);color:var(--white);font-family:var(--sans);font-size:10px;font-weight:700;display:flex;align-items:center;justify-content:center;text-transform:uppercase}
.dots{position:absolute;top:757px;left:536px;display:flex;gap:8px}
.dots span{width:36px;height:3px;background:rgba(255,255,255,.45)}
.dots .on{background:var(--white)}

/* intro */
.intro{height:205px;background:#f2f2f2}
.intro h2{position:absolute;left:161px;top:66px;width:290px;font-family:var(--sans);font-weight:600;font-size:21px;line-height:33px;color:var(--ink)}
.intro .col{position:absolute;top:54px;font-size:10px;line-height:22px}
.initial{float:left;width:48px;height:48px;background:var(--orange);color:var(--white);font-family:var(--sans);font-weight:700;font-size:24px;display:flex;align-items:center;justify-content:center;margin:6px 14px 4px 0}

/* company */
.company{height:585px}
.skill{position:absolute;left:161px;width:425px;font-family:var(--sans);font-size:10px;color:var(--ink)}
.skill .pct{position:absolute;right:0;top:0}
.skill .track{position:absolute;top:22px;left:0;width:100%;height:1px;background:#ddd}
.skill .fill{position:absolute;top:-1px;left:0;height:3px;background:var(--ink)}
.company .frame{position:absolute;left:656px;top:81px;width:382px;height:424px;background:#fff;box-shadow:0 0 8px rgba(0,0,0,.18);padding:6px}
.company .frame .img{width:100%;height:100%;background:
  radial-gradient(ellipse 70px 150px at 150px 200px,rgba(180,190,200,.55),transparent 70%),
  radial-gradient(ellipse 70px 150px at 230px 210px,rgba(40,60,90,.7),transparent 70%),
  repeating-linear-gradient(90deg,rgba(120,170,230,.12) 0 2px,transparent 2px 26px),
  linear-gradient(180deg,#101a28 0%,#1b2d46 55%,#4d7aaa 85%,#6f9bcb 100%)}
.company .frame .logo{position:absolute;left:88px;top:185px;color:var(--white);font-size:22px;line-height:26px;width:220px;gap:10px}
.company .frame .logo-mark{background:var(--white);width:18px;height:18px}

/* practice */
.practice{height:563px;background:var(--light)}
.card{position:absolute;top:173px;width:277px;height:263px}
.card .img{width:100%;height:100%}
.card .cap{position:absolute;left:0;bottom:0;width:100%;height:60px;background:rgba(30,30,30,.82);color:var(--white);font-family:var(--sans);font-size:12px;font-weight:700;display:flex;align-items:center;justify-content:center}
.explore{position:absolute;top:470px;font-family:var(--sans);font-size:10px;color:var(--ink)}
.explore span{text-decoration:underline}

/* cta */
.cta{height:264px;background:
  radial-gradient(ellipse 260px 140px at 640px 220px,rgba(120,120,120,.35),transparent 70%),
  radial-gradient(ellipse 220px 160px at 1050px 60px,rgba(160,160,160,.3),transparent 70%),
  linear-gradient(100deg,#232323 0%,#333 50%,#4a4c4f 100%)}
.cta h2{position:absolute;left:161px;top:80px;font-family:var(--sans);font-weight:700;font-size:24px;color:var(--white)}
.cta p{position:absolute;left:161px;top:126px;width:560px;font-size:10px;line-height:22px;color:#eee}

/* why */
.why{height:708px}
.box{position:absolute;padding:36px 30px}
.box h3{font-family:var(--sans);font-weight:400;font-size:15px;margin-bottom:14px}
.box p{font-size:9px;line-height:22px}
.box .more{margin-top:10px;font-family:var(--sans);font-size:9px;display:flex;align-items:center;gap:6px}
.box.grey{background:#e4e4e4;color:#666}
.box.grey h3,.box.grey .more{color:var(--ink)}
.box.dark{background:#2e2e2e;color:#ccc}
.box.dark h3,.box.dark .more{color:var(--white)}

/* experts */
.experts{height:590px;background:linear-gradient(#ececec 0,#ececec 329px,#fff 329px)}
.expert{position:absolute;top:177px;width:198px;text-align:center}
.expert .pic{height:258px;border:4px solid #fff;box-shadow:0 0 3px rgba(0,0,0,.15)}
.expert h4{margin-top:28px;font-family:var(--sans);font-weight:400;font-size:13px;color:var(--ink)}
.expert small{display:block;margin-top:6px;font-size:9px;text-transform:uppercase;color:#777}

/* careers */
.careers{height:576px;background:
  radial-gradient(ellipse 130px 170px at 820px 140px,rgba(215,175,150,.35),transparent 70%),
  radial-gradient(ellipse 160px 260px at 830px 420px,rgba(35,55,90,.75),transparent 70%),
  radial-gradient(ellipse 150px 260px at 1040px 400px,rgba(175,135,95,.6),transparent 70%),
  radial-gradient(ellipse 180px 120px at 880px 400px,rgba(235,235,240,.45),transparent 70%),
  linear-gradient(90deg,#2a2e33 0%,#353b42 45%,#5d6874 62%,#8a95a1 82%,#59616b 100%)}
.acc{position:absolute;left:161px;width:426px;height:42px;background:rgba(255,255,255,.14);border:1px solid rgba(255,255,255,.25);font-family:var(--sans);font-size:12px;font-weight:600;color:var(--white);display:flex;align-items:center;justify-content:space-between;padding:0 18px}
.acc.open{color:var(--orange)}
.panel{position:absolute;left:161px;width:426px;padding:16px 18px;border:1px solid rgba(255,255,255,.25);border-top:0;font-size:10px;line-height:22px;color:#eee}

/* news */
.news{height:672px}
.post{position:absolute;top:182px;width:264px}
.post .img{height:241px;position:relative;box-shadow:0 0 4px rgba(0,0,0,.15)}
.post .tag{position:absolute;right:10px;top:8px;background:var(--orange);color:var(--white);font-family:var(--sans);font-size:8px;font-weight:700;padding:8px 10px}
.post .meta{margin-top:27px;font-family:var(--sans);font-size:8px;color:#888}
.post h4{margin-top:8px;font-family:var(--sans);font-weight:700;font-size:12px;line-height:22px;color:var(--ink)}
.post p{margin-top:9px;font-size:9px;line-height:22px}
.post .link{margin-top:12px;font-family:var(--sans);font-size:8px;color:var(--orange);display:flex;align-items:center;gap:6px}

/* footer */
.footer{height:422px;background:var(--dark);color:#ddd}
.footer .about{position:absolute;left:161px;top:150px;width:160px;font-size:10px;line-height:22px}
.fcol{position:absolute;top:76px}
.fcol h5{font-family:var(--serif);font-weight:700;font-size:18px;color:var(--white);margin-bottom:16px}
.fcol li{list-style:none;font-family:var(--serif);font-size:10px;color:#ddd;height:33px;display:flex;align-items:flex-start;gap:6px}
.fcol li::before{content:"»";color:var(--orange)}
.contact li::before{content:none}
.copy{position:absolute;top:390px;font-size:10px;color:var(--white)}
.copy b{color:var(--orange);font-weight:700}
</style>
</head>
<body>

<section class="section hero" role="img" aria-label="Photo of a consulting team reviewing data charts on a screen">
  <div class="abs topbar">
    <div class="item" style="left:161px">
      <svg width="10" height="10" viewBox="0 0 24 24"><path fill="#f58a3c" d="M6.6 10.8a15 15 0 006.6 6.6l2.2-2.2c.3-.3.7-.4 1-.2 1.1.4 2.3.6 3.6.6.6 0 1 .4 1 1V20c0 .6-.4 1-1 1A17 17 0 013 4c0-.6.4-1 1-1h3.5c.6 0 1 .4 1 1 0 1.3.2 2.5.6 3.6.1.3 0 .7-.2 1z"/></svg>
      +44 20 5550 1947
    </div>
    <div class="item" style="left:278px">
      <svg width="10" height="8" viewBox="0 0 24 18"><rect width="24" height="18" fill="#f58a3c"/><path d="M0 0l12 9 12-9" fill="none" stroke="#1c1c1c" stroke-width="2"/></svg>
      info@halvernridge.com
    </div>
    <span class="social" style="left:988px"></span>
    <span class="social" style="left:1014px"></span>
  </div>
  <header class="abs nav">
    <div class="logo"><span class="logo-mark"></span>Halvern Ridge Advisory LLC</div>
    <nav class="menu">
      <span class="active">Home</span><span>About Halvern</span><span>Our Experts</span><span>News and Events</span><span>Careers</span><span>Contact Us</span>
    </nav>
  </header>
  <div class="abs eyebrow">Welcome to Halvern Ridge Advisory LLC</div>
  <h1>YOUR PARTNER IN CYBER-SECURITY</h1>
  <p>Nemo enim ipsam voluptatem quia voluptas sit aspernatur aut odit aut fugit, quia consequuntur magni dolores eos qui ratione voluptatem sequi nesciunt. Neque porro quisquam est, qui dolorem ipsum quia dolor sit amet, consectetur</p>
  <div class="btn" style="left:161px;top:540px;width:128px;height:47px">Learn More</div>
  <div class="dots"><span></span><span class="on"></span><span></span></div>
</section>

<section class="section intro">
  <h2>Introduction of Halvern Ridge Advisory</h2>
  <div class="col" style="left:463px;width:275px">
    <div class="initial">H</div>
    Halvern Ridge Advisory is dolor sit amet, consectetur adipiscing elit, sed do eiusmod tempor incididunt ut laboreet et alvero eos et accusamus et iusto odio dignissimos
  </div>
  <div class="col" style="left:760px;width:279px">Quis autem vel eum iure reprehenderit qui in ea voluptate velit essef quam nihil molestiae  estor consequatur, vel illum qui dolorem eum fugiat quo voluptas nulla pariatur?</div>
</section>

<section class="section company">
  <div class="abs eyebrow" style="left:161px;top:105px">About Halvern</div>
  <h2 class="abs title" style="left:161px;top:118px">Our Company</h2>
  <p class="abs body" style="left:161px;top:172px;width:440px;font-size:10px">Sed ut perspiciatis unde omnis iste natus error sit voluptatem accusantium doloremque laudantium, totam rem aperiam, eaque ipsa quae ab illo inventore veritatis et quasi architecto beatae vitae dicta sunt explicabo.</p>
  <div class="skill" style="top:256px">IT Solutions<span class="pct">90%</span><div class="track"><div class="fill" style="width:90%"></div></div></div>
  <div class="skill" style="top:299px">Cyber Security<span class="pct">95%</span><div class="track"><div class="fill" style="width:95%"></div></div></div>
  <div class="skill" style="top:343px">Risk &amp; Project Managment<span class="pct">92%</span><div class="track"><div class="fill" style="width:92%"></div></div></div>
  <div class="skill" style="top:386px">Data Analytics Consulting<span class="pct">92%</span><div class="track"><div class="fill" style="width:92%"></div></div></div>
  <p class="abs body" style="left:161px;top:436px;width:440px;font-size:10px">Sed ut perspiciatis unde omnis iste natus error sit voluptatem accusantium doloremque laudantium.</p>
  <div class="frame">
    <div class="img" role="img" aria-label="Photo of two consultants in a server room"></div>
    <span class="logo"><span class="logo-mark"></span>Halvern Ridge Advisory LLC</span>
  </div>
</section>

<section class="section practice">
  <div class="abs eyebrow center" style="top:80px">What do we offer</div>
  <h2 class="abs title center" style="top:94px">Areas of Practice</h2>
  <div class="card" style="left:161px"><div class="img" role="img" aria-label="Photo of an analyst at screens showing a world map" style="background:radial-gradient(ellipse 90px 70px at 110px 110px,rgba(140,200,255,.6),transparent 70%),radial-gradient(ellipse 80px 90px at 150px 200px,rgba(15,25,40,.9),transparent 70%),repeating-linear-gradient(90deg,rgba(90,150,220,.15) 0 2px,transparent 2px 22px),linear-gradient(160deg,#0c223d,#1f4e80 55%,#13304f)"></div><div class="cap">Cyber Security</div></div>
  <div class="card" style="left:462px"><div class="img" role="img" aria-label="Photo of a project meeting over documents" style="background:radial-gradient(ellipse 110px 70px at 170px 150px,rgba(225,220,210,.55),transparent 70%),radial-gradient(ellipse 110px 120px at 70px 80px,rgba(40,38,36,.8),transparent 70%),linear-gradient(160deg,#7b756d,#3e3a36 60%,#5e564e)"></div><div class="cap">Project Managment</div></div>
  <div class="card" style="left:761px"><div class="img" role="img" aria-label="Photo of an engineer in a data centre aisle" style="background:radial-gradient(ellipse 40px 90px at 140px 120px,rgba(200,190,170,.5),transparent 70%),radial-gradient(ellipse 60px 140px at 140px 90px,rgba(230,230,230,.35),transparent 70%),repeating-linear-gradient(90deg,rgba(255,255,255,.05) 0 3px,transparent 3px 18px),linear-gradient(90deg,#1f1f1f,#4a4a4a 50%,#1f1f1f)"></div><div class="cap">Data Analytics Solutions</div></div>
  <div class="explore center">+ <span>EXPLORE ALL</span></div>
</section>

<section class="section cta" role="img" aria-label="Dark photo of a business meeting">
  <h2>Got any project you would like to discuss?</h2>
  <p>Quis autem vel eum iure reprehenderit qui in ea voluptate velit essef quam nihil molestiae  estor consequatur, vel illum qui dolorem eum fugiat quo voluptas nulla pariatur?</p>
  <div class="btn" style="left:910px;top:111px;width:128px;height:46px">Contact Us</div>
</section>

<section class="section why">
  <div class="abs eyebrow center" style="top:75px">Our Features</div>
  <h2 class="abs title center" style="top:89px">Why People Choose Us</h2>
  <div class="box grey" style="left:161px;top:179px;width:278px;height:186px">
    <h3>Our Mission</h3>
    <p>Sed ut perspiciatis unde omnis iste tus error sit voluptatem accusantium esterlla doloremque laudantium, totam rem</p>
    <div class="more">DISCOVER <svg width="16" height="6" viewBox="0 0 16 6"><path d="M0 3h14M11 0l3 3-3 3" stroke="currentColor" fill="none"/></svg></div>
  </div>
  <div class="box dark" style="left:461px;top:179px;width:278px;height:186px">
    <h3>Our Target</h3>
    <p>Sed ut perspiciatis unde omnis iste tus error sit voluptatem accusantium esterlla doloremque laudantium, totam rem</p>
    <div class="more">DISCOVER <svg width="16" height="6" viewBox="0 0 16 6"><path d="M0 3h14M11 0l3 3-3 3" stroke="currentColor" fill="none"/></svg></div>
  </div>
  <div class="abs" role="img" aria-label="Photo of two businessmen reviewing a document" style="left:761px;top:179px;width:277px;height:448px;background:radial-gradient(ellipse 60px 110px at 90px 170px,rgba(30,40,60,.75),transparent 70%),radial-gradient(ellipse 60px 110px at 190px 160px,rgba(60,65,72,.75),transparent 70%),linear-gradient(180deg,#c9cdd2 0%,#8e959d 35%,#3c3c3c 60%,#2b2b2b 100%)"></div>
  <div class="box" style="left:761px;top:420px;width:277px;padding:0 30px;color:#ddd">
    <h3 style="color:#fff">Our Workflow</h3>
    <p>Sed ut perspiciatis unde omnis iste tus error sit voluptatem accusantium esterlla doloremque laudantium, totam rem</p>
    <div class="more" style="color:#fff">DISCOVER <svg width="16" height="6" viewBox="0 0 16 6"><path d="M0 3h14M11 0l3 3-3 3" stroke="currentColor" fill="none"/></svg></div>
  </div>
  <div class="abs" role="img" aria-label="Video still of an operations room with large data screens" style="left:161px;top:389px;width:578px;height:238px;background:radial-gradient(ellipse 200px 60px at 290px 190px,rgba(20,25,35,.85),transparent 70%),radial-gradient(ellipse 130px 70px at 480px 80px,rgba(120,180,240,.55),transparent 70%),repeating-linear-gradient(90deg,rgba(120,180,240,.12) 0 2px,transparent 2px 30px),linear-gradient(120deg,#13253b,#2f5580 50%,#1a2c42)"></div>
  <svg class="abs" style="left:419px;top:477px" width="62" height="62" viewBox="0 0 62 62"><circle cx="31" cy="31" r="31" fill="rgba(255,255,255,.55)"/><path d="M25 20l17 11-17 11z" fill="#fff"/></svg>
</section>

<section class="section experts">
  <div class="abs eyebrow center" style="top:75px">Meet the team members</div>
  <h2 class="abs title center" style="top:89px">Our Experts</h2>
  <div class="expert" style="left:161px"><div class="pic" role="img" aria-label="Portrait of the chief executive in a beige blazer" style="background:radial-gradient(ellipse 80px 110px at 50% 92%,#b9a58f,transparent 75%),radial-gradient(ellipse 30px 36px at 50% 28%,#cdb4a2,transparent 75%),linear-gradient(#f0f0f0,#dcdcdc)"></div><h4>Owen Castell</h4><small>CEO-Founder</small></div>
  <div class="expert" style="left:388px"><div class="pic" role="img" aria-label="Portrait of the cyber security expert in a grey suit holding a laptop" style="background:radial-gradient(ellipse 80px 110px at 50% 92%,#a9a9aa,transparent 75%),radial-gradient(ellipse 50px 30px at 50% 70%,#3a3a3c,transparent 75%),radial-gradient(ellipse 30px 36px at 50% 22%,#c9a994,transparent 75%),linear-gradient(#f0f0f0,#dcdcdc)"></div><h4>Reid Marlow</h4><small>Cyber Security Expert</small></div>
  <div class="expert" style="left:614px"><div class="pic" role="img" aria-label="Portrait of the business consultant in a navy suit" style="background:radial-gradient(ellipse 80px 120px at 50% 92%,#1f2a44,transparent 75%),radial-gradient(ellipse 30px 36px at 50% 25%,#d1ad93,transparent 75%),linear-gradient(#f0f0f0,#dcdcdc)"></div><h4>Tomas Vell</h4><small>Business Consultant</small></div>
  <div class="expert" style="left:840px"><div class="pic" role="img" aria-label="Portrait of the IT specialist in a navy shirt" style="background:radial-gradient(ellipse 85px 120px at 50% 92%,#2b3752,transparent 75%),radial-gradient(ellipse 30px 36px at 50% 25%,#c9a48a,transparent 75%),linear-gradient(#f0f0f0,#dcdcdc)"></div><h4>Adrian Kole</h4><small>IT Specialist</small></div>
</section>

<section class="section careers" role="img" aria-label="Photo of two young professionals looking at a laptop">
  <div class="abs eyebrow" style="left:161px;top:64px">Our Approach</div>
  <h2 class="abs title" style="left:161px;top:77px;color:#fff">Careers</h2>
  <p class="abs body" style="left:161px;top:122px;width:430px;font-size:10px;color:#eee">Quis autem vel eum iure reprehenderit qui in ea voluptate velit essef quam nihil molestiae  estor consequatur.</p>
  <div class="acc" style="top:190px">Lorem Ipsum Dolor<span>+</span></div>
  <div class="acc open" style="top:243px">Simply Dummy Text<span>-</span></div>
  <div class="panel" style="top:285px">Quis autem vel eum iure reprehenderit qui in ea voluptate velit essef quam nihil molestiae  estor consequatur, vel illum qui dolorem eum fugiat quo voluptas nulla pariatur?</div>
  <div class="acc" style="top:403px">Text Filler Design Purposes<span>+</span></div>
  <div class="acc" style="top:456px">Dolor Amet Valar Morghulis<span>+</span></div>
</section>

<section class="section news">
  <div class="abs eyebrow center" style="top:78px">Recent blog posts</div>
  <h2 class="abs title center" style="top:92px">News and Events</h2>
  <article class="post" style="left:168px">
    <div class="img" role="img" aria-label="Photo of colleagues at computers in an office" style="background:radial-gradient(ellipse 70px 60px at 90px 120px,rgba(40,50,70,.7),transparent 70%),radial-gradient(ellipse 90px 50px at 180px 180px,rgba(60,60,60,.6),transparent 70%),linear-gradient(180deg,#e6e6e6 0%,#b5b5b5 45%,#6a6a6a 100%)"><span class="tag">IT SOLUTIONS</span></div>
    <div class="meta">BY: ADMIN &nbsp;|&nbsp; ON: 27th DEC, 2020</div>
    <h4>Lorem ipsum is a simply dummy text used for design purposes</h4>
    <p>Excepteur sint occaecat cupidatat if non offer the proident, sunt in culpa qui officerunt eld..</p>
    <div class="link">READ FULL STORY <svg width="14" height="6" viewBox="0 0 14 6"><path d="M0 3h12M9 0l3 3-3 3" stroke="currentColor" fill="none"/></svg></div>
  </article>
  <article class="post" style="left:468px">
    <div class="img" role="img" aria-label="Photo of a man behind blue data projections" style="background:radial-gradient(ellipse 70px 90px at 150px 170px,rgba(10,15,25,.85),transparent 70%),repeating-linear-gradient(0deg,rgba(130,200,255,.14) 0 2px,transparent 2px 14px),linear-gradient(160deg,#0b1d36,#2a67a3 55%,#0e2643)"><span class="tag">CYBERSECURITY</span></div>
    <div class="meta">BY: ADMIN &nbsp;|&nbsp; ON: 18th DEC, 2020</div>
    <h4>Lorem ipsum is a simply dummy text used for design purposes</h4>
    <p>Excepteur sint occaecat cupidatat if non offer the proident, sunt in culpa qui officerunt eld..</p>
    <div class="link">READ FULL STORY <svg width="14" height="6" viewBox="0 0 14 6"><path d="M0 3h12M9 0l3 3-3 3" stroke="currentColor" fill="none"/></svg></div>
  </article>
  <article class="post" style="left:760px">
    <div class="img" role="img" aria-label="Photo of a smiling business team in an office" style="background:radial-gradient(ellipse 50px 90px at 80px 170px,rgba(40,50,75,.7),transparent 70%),radial-gradient(ellipse 50px 90px at 190px 170px,rgba(60,60,65,.65),transparent 70%),radial-gradient(ellipse 50px 90px at 135px 160px,rgba(245,245,245,.8),transparent 70%),linear-gradient(180deg,#f2f2f2,#c4c7ca 60%,#8a8e93)"><span class="tag">PROJECT RISK</span></div>
    <div class="meta">BY: ADMIN &nbsp;|&nbsp; ON: 20th DEC, 2020</div>
    <h4>Lorem ipsum is a simply dummy text used for design purposes</h4>
    <p>Excepteur sint occaecat cupidatat if non offer the proident, sunt in culpa qui officerunt eld..</p>
    <div class="link">READ FULL STORY <svg width="14" height="6" viewBox="0 0 14 6"><path d="M0 3h12M9 0l3 3-3 3" stroke="currentColor" fill="none"/></svg></div>
  </article>
</section>

<footer class="section footer">
  <div class="abs logo" style="left:161px;top:80px;font-size:16px;line-height:19px;width:180px"><span class="logo-mark"></span>Halvern Ridge Advisory LLC</div>
  <p class="about">Nemo enim ipsam voluptatem quia voluptas sit aspernatur aut odit aut fugit, sed quia consequuntur magni dolores eos qui ratione voluptatem sequi nesciunt. Neque porro quisquam est, qui dolorem ipsum quia dolor sit</p>
  <div class="fcol" style="left:386px"><h5>Quick Links</h5><ul><li>About Us</li><li>Our Experts</li><li>News And Events</li><li>Careers</li><li>Contact</li></ul></div>
  <div class="fcol" style="left:610px"><h5>Information</h5><ul><li>Sitemap</li><li>Terms Of Use</li><li>Privacy &amp; Policy</li><li>Lorem Ipsum</li><li>Text Filler</li></ul></div>
  <div class="fcol contact" style="left:836px"><h5>Contact</h5><ul>
    <li style="height:44px;line-height:16px"><svg width="9" height="12" viewBox="0 0 9 12"><path d="M4.5 0A4.5 4.5 0 000 4.5C0 8 4.5 12 4.5 12S9 8 9 4.5A4.5 4.5 0 004.5 0zm0 6.3a1.8 1.8 0 110-3.6 1.8 1.8 0 010 3.6z" fill="#f58a3c"/></svg><span>Lorem Ipsum Street, Avenue 201<br>United States</span></li>
    <li style="height:28px"><svg width="10" height="10" viewBox="0 0 24 24"><path fill="#f58a3c" d="M6.6 10.8a15 15 0 006.6 6.6l2.2-2.2c.3-.3.7-.4 1-.2 1.1.4 2.3.6 3.6.6.6 0 1 .4 1 1V20c0 .6-.4 1-1 1A17 17 0 013 4c0-.6.4-1 1-1h3.5c.6 0 1 .4 1 1 0 1.3.2 2.5.6 3.6.1.3 0 .7-.2 1z"/></svg>+44 20 5550 1947</li>
    <li><svg width="10" height="8" viewBox="0 0 24 18"><rect width="24" height="18" fill="#f58a3c"/><path d="M0 0l12 9 12-9" fill="none" stroke="#262626" stroke-width="2"/></svg>info@halvernridge.com</li>
  </ul></div>
  <div class="copy center" style="text-align:center">Copyright © 2020 <b>Halvern Ridge Advisory LLC</b> - All Rights Reserved</div>
</footer>

</body>
</html>
```